Insurance Law Website

**Please note do not sell insurance, we are a law firm which specialises in Insurance law.**

We are a legal insurance firm based in Australia consisting of 150+ legal professionals.

Our initial budget for this project is around: $500

We require a design to meet the specification below, however we do want designers to come up with an interpretation of something modern but still professional, we need it to stand out above all other legal websites!

1. Responsive design
2. It should be a minimalist design, the use of background imagery is fine but we are looking to de-clutter the home page in particular and have additional content accessible through menu links to other areas such as publications, news, announcements and expert/staff pages, careers etc.
3. Something that stands out from a typical legal website.
4. The homepage should cater for a video which will contain a 'who we are' message from the CEO/Firm.
5. Colours used light/medium blues (eg: #8aabff, #bdd7fc), white
6. We also require a static information box on the page with the heading "THREE STATES, ONE FOCUS" - see image attached for full text of the box.

Visitors to our website should be aware we are an Insurance law firm, this can be achieved by using insurance focused full background imagery (no natural disasters such as floods, earthquakes etc) such as insurance buildings (Harwick building - London), international landmarks etc

Some websites we like certain aspects of;

http://pellambraithwaite.com/ - top image boxes
http://www.vantel.com.au/ - similar however prefer to use a FULL background image, with one full width text box at the bottom, navigation menu at the top with logo

However please don't take these examples as a sign of what the site MUST look like, please use your imagination to interpret your own vision.

Reason: Extended due to feedback provided and waiting for resubmission of designs. It appears that some people may be misunderstanding the brief, please review the brief in full before submitting any designs and let us know if you have any questions.

Reason: Apologies to those who are waiting for a decision we are reviewing and discussiing all submitted designs internally and waiting for some additional amendments to come in. We have extended the project a final time whilst we carry out our reviews. Please continue to submit any modifications and thanks again for everyone's input thus far. D+T

We have 3 days left of this project please keep submitting your designs. This is a guaranteed project.

D+T

Target Market(s)

Lawyers looking for publications, information, contact details of our lawyers and careers/job searches.

Industry/Entity Type

Insurance

Font styles to use
Sans Serif

Requirements
Must have
• Top menu to include:

Home (small icon)
Who We Are (text)
Experts (text)
Expertise (text)
Media (text)
- News (text)
- Publications (text)
Community Footprint (text)
Careers (text)
Contact (text/icon)
Search (icon - will expand on click to search in field)

Footer to include:

Copyright (text)
Privacy Policy (text)
Cookie policy (text)
Sitemap (text)
Contact (text/icon)
Chainbook (icon)
Print (icon)
Email (icon)

Should not have
• Stereotypical imagery such as legal scales, money bags, natural disasters etc. We are a professional firm and require designs to suit.

```html
<!DOCTYPE html>
<html lang="en">
<head>
<meta charset="utf-8">
<title>Dalton Trask — Insurance Law</title>
<link rel="stylesheet" href="https://fonts.googleapis.com/css2?family=Arimo:wght@400;700&display=swap">
<style>
  :root {
    --brand-navy: #1c3f94;
    --brand-blue: #1f56a8;
    --nav-text: #1d3f8f;
    --panel-blue: rgba(189, 215, 252, 0.88);
    --header-bg: #f4f5f8;
    --footer-bg: #eef0f4;
    --body-text: #1b2a52;
    --hero-dark: #3e4349;
    --hero-mid: #9a9ea4;
    --hero-light: #eceded;
    --white: #ffffff;
  }
  * { box-sizing: border-box; margin: 0; padding: 0; }
  html, body {
    width: 1200px; height: 900px; overflow: hidden;
    font-family: "Arimo", Arial, sans-serif;
    background: var(--white);
  }
  .page { position: relative; width: 1200px; height: 900px; overflow: hidden; }

  /* Header */
  .site-header {
    position: absolute; top: 0; left: 0; width: 1200px; height: 132px;
    background: var(--header-bg);
  }
  .brand {
    position: absolute; left: 36px; top: 26px;
    color: var(--brand-navy); font-weight: 400; font-size: 44px; line-height: 40px;
    letter-spacing: 0.5px;
  }
  .main-nav { position: absolute; top: 92px; left: 0; width: 1200px; height: 26px; }
  .main-nav a, .main-nav .nav-icon {
    position: absolute; top: 0; color: var(--nav-text); text-decoration: none;
    font-size: 15.5px; line-height: 24px;
  }

  /* Hero */
  .hero {
    position: absolute; top: 132px; left: 0; width: 1200px; height: 713px;
    background:
      radial-gradient(ellipse 420px 300px at 620px 220px, rgba(255,255,255,0.55), rgba(255,255,255,0) 70%),
      linear-gradient(200deg, rgba(40,44,50,0.55) 0%, rgba(40,44,50,0) 35%),
      linear-gradient(125deg, var(--hero-light) 0%, #d4d6d8 40%, var(--hero-mid) 62%, #6c7076 82%, var(--hero-dark) 100%);
  }
  .focus-mark { position: absolute; left: 386px; top: 26px; }
  .focus-box { position: absolute; left: 430px; top: 56px; width: 520px; }
  .focus-box h1 { color: var(--brand-blue); font-size: 40px; font-weight: 700; line-height: 46px; }
  .focus-box p { margin-top: 12px; color: #111; font-size: 16px; line-height: 20px; }

  /* Side panel */
  .side-panel {
    position: absolute; left: 36px; top: 0; width: 287px; height: 713px;
    background: var(--panel-blue);
  }
  .video-frame {
    position: absolute; left: 15px; top: 18px; width: 254px; height: 252px;
    background: linear-gradient(160deg, #9fb4c9 0%, #d8dde4 45%, #7f8ea0 100%);
  }
  .video-frame svg { position: absolute; left: 77px; top: 76px; }
  .teaser { position: absolute; left: 19px; width: 240px; }
  .teaser h2 { font-size: 24px; font-weight: 700; line-height: 28px; color: var(--brand-navy); }
  .teaser p { margin-top: 8px; font-size: 15.5px; line-height: 20px; color: var(--brand-blue); }
  .teaser .read-more { display: block; margin-top: 10px; font-size: 15.5px; line-height: 20px; color: var(--brand-navy); text-decoration: none; }
  .teaser-people { top: 298px; }
  .teaser-news { top: 515px; }
  .divider {
    position: absolute; left: 0; top: 498px; width: 287px;
    border-top: 1px dashed rgba(31, 86, 168, 0.55);
  }

  /* Footer */
  .site-footer {
    position: absolute; top: 845px; left: 0; width: 1200px; height: 55px;
    background: var(--footer-bg); font-size: 12px; color: var(--body-text);
  }
  .site-footer .copyright { position: absolute; left: 54px; top: 20px; }
  .site-footer a { position: absolute; top: 20px; color: var(--nav-text); text-decoration: none; }
  .footer-icons { position: absolute; left: 1034px; top: 17px; display: flex; gap: 4px; }
  .footer-icons svg { display: block; }
  .social-name {
    height: 20px; padding: 0 6px; background: var(--nav-text); color: var(--white);
    font-size: 10.5px; line-height: 20px;
  }
</style>
</head>
<body>
<div class="page">

  <header class="site-header">
    <div class="brand">dalton<br>trask</div>
    <nav class="main-nav">
      <span class="nav-icon" style="left:394px;" aria-label="Home">
        <svg width="20" height="20" viewBox="0 0 20 20"><path d="M2 10 L10 3 L18 10 L16 10 L16 18 L11.5 18 L11.5 13 L8.5 13 L8.5 18 L4 18 L4 10 Z" fill="#6e6a9a"/></svg>
      </span>
      <a style="left:450px">Who We Are</a>
      <a style="left:564px">Experts</a>
      <a style="left:645px">Expertise</a>
      <a style="left:738px">Media</a>
      <a style="left:807px">Community</a>
      <a style="left:913px">Footprint</a>
      <a style="left:1002px">Careers</a>
      <a style="left:1086px">Contact</a>
      <span class="nav-icon" style="left:1162px;" aria-label="Search">
        <svg width="22" height="22" viewBox="0 0 22 22"><circle cx="9" cy="9" r="6.5" fill="none" stroke="#1d3f8f" stroke-width="2.4"/><line x1="13.8" y1="13.8" x2="20" y2="20" stroke="#1d3f8f" stroke-width="3" stroke-linecap="round"/></svg>
      </span>
    </nav>
  </header>

  <main class="hero" role="img" aria-label="Black and white upward view of a modern insurance building with steel frames and glass towers">
    <aside class="side-panel">
      <div class="video-frame" role="img" aria-label="Video still of the firm's chief executive speaking, office background">
        <svg width="100" height="100" viewBox="0 0 100 100"><circle cx="50" cy="50" r="45" fill="none" stroke="#ffffff" stroke-width="3"/><path d="M38 28 L72 50 L38 72 Z" fill="none" stroke="#ffffff" stroke-width="3"/></svg>
      </div>
      <section class="teaser teaser-people">
        <h2>People</h2>
        <p>Lorem ipsum dolor sit amet, consectetur adipiscing elit. Vivamus quis luctus lectus, nec dictum ligula. Nunc feugiat pellentesque dolor viverra.</p>
        <a class="read-more">&gt; Read more</a>
      </section>
      <div class="divider"></div>
      <section class="teaser teaser-news">
        <h2>News</h2>
        <p>Lorem ipsum dolor sit amet, consectetur adipiscing elit. Vivamus quis luctus lectus, nec dictum ligula. Nunc feugiat pellentesque dolor viverra.</p>
        <a class="read-more">&gt; Read more</a>
      </section>
    </aside>

    <svg class="focus-mark" width="50" height="50" viewBox="0 0 50 50" aria-hidden="true">
      <line x1="24" y1="0" x2="24" y2="48" stroke="#1f56a8" stroke-width="1.5"/>
      <line x1="0" y1="24" x2="48" y2="24" stroke="#1f56a8" stroke-width="1.5"/>
    </svg>

    <section class="focus-box">
      <h1>Three states. One focus.</h1>
      <p>Our sole focus is insurance law and we act for a diverse range of risk carriers, underwriting agents, brokers and corporate insureds relevant to litigious and general advisory services.</p>
    </section>
  </main>

  <footer class="site-footer">
    <span class="copyright">© All rights reserved 2014</span>
    <a style="left:768px">Privacy Policy</a>
    <a style="left:876px">Cookie policy</a>
    <a style="left:978px">Sitemap</a>
    <div class="footer-icons">
      <svg width="20" height="20" viewBox="0 0 20 20" aria-label="Accessibility"><rect width="20" height="20" fill="#1d3f8f"/><circle cx="10" cy="4.5" r="1.8" fill="#fff"/><path d="M5 8 H15 M10 8 V12 L6.5 16.5 M10 12 L13.5 16.5" stroke="#fff" stroke-width="1.8" fill="none"/></svg>
      <span class="social-name">Chainbook</span>
      <svg width="20" height="20" viewBox="0 0 20 20" aria-label="Print"><rect width="20" height="20" fill="#1d3f8f"/><rect x="6" y="3.5" width="8" height="4" fill="#fff"/><rect x="3.5" y="8" width="13" height="6" fill="#fff"/><rect x="6" y="12" width="8" height="5" fill="#fff" stroke="#1d3f8f" stroke-width="1"/></svg>
      <svg width="20" height="20" viewBox="0 0 20 20" aria-label="Email"><rect width="20" height="20" fill="#1d3f8f"/><rect x="3.5" y="5.5" width="13" height="9" fill="#fff"/><path d="M3.5 5.5 L10 11 L16.5 5.5" stroke="#1d3f8f" stroke-width="1.3" fill="none"/></svg>
    </div>
  </footer>

</div>
</body>
</html>
```